demask background, dbl page ad for magazine, specific design instructions

INCREASED BUDGET!! :) URGENT DESIGN REQUIRED.
double page print ad for a wedding photography business going in a small sized hardcover magazine called THE VOW PLANNER in Perth Western Australia.
specs: 336mmx210mm (over double page) please use 3mm bleed.
Biz name: Seabreeze by Anton
Designers please use InDesign if possible.
THREE ATTACHMENTS INCLUDED, all already converted to CMYK
FONT
century gothic size 12 font
I will attach the two images to use
____________
AD DESIGN
(1) colour image is full page on right, can bleed off on left page if possible. Caption font 10, century gothic to say "Seabreeze by Anton" on bottom left.
(2) Left hand page background to be a demask dark purple and light purple transitioning from pure dark purple on left hand side of left page to a subtle demask pattern. Dark purple to be CMYK: 80/100/0/70. lighter purple to be CMYK: 80/100/0/0
(3) Logo to take up half the width of l-h-s page, position at top of page
(4) contact details to read as follows centred: (white)
Anton (size 14)
04 827 39 516 (size 12)
www.amfoto.com.au (size 12)
[facebook symbol] seabreezebyanton (size 12)
(5) under contact details, to insert a small black and white image
(6) headline: Live, Dream, Love, Share in a very subtle colour, suiteable font, size 16
Target Market(s)
SECONDARY target market is: wedding businesses,
PRIMARY target is: more sophisticated bride, middle to high income, women between the ages of 28-35 yrs
Industry/Entity Type
Wedding
Look and feel
Each slider illustrates characteristics of the customer's brand and the style your logo design should communicate.

```html
<!DOCTYPE html>
<html lang="en">
<head>
<meta charset="utf-8">
<title>Seabreeze by Anton – Magazine Ad</title>
<link href="https://fonts.googleapis.com/css2?family=Questrial&family=Great+Vibes&display=swap" rel="stylesheet">
<style>
  :root {
    --backdrop: #ffffff;
    --purple-deep: #1c0a22;
    --purple-dark: #2d0f38;
    --purple-mid: #4e1c63;
    --purple-glow: #6a2a86;
    --logo-tint: #9b86a6;
    --contact-white: #e6def0;
    --headline-tint: #c9b9d6;
    --photo-dark: #141414;
    --photo-light: #9a9a9a;
    --sky: #b9c6d4;
    --foliage: #6f7a45;
  }
  * { box-sizing: border-box; margin: 0; padding: 0; }
  html, body {
    width: 1200px; height: 901px; overflow: hidden;
    background: var(--backdrop);
  }
  .spread {
    position: absolute; left: 289px; top: 76px;
    width: 654px; height: 741px;
    display: flex;
  }
  .left-page {
    position: relative; width: 594px; height: 741px;
    background: radial-gradient(ellipse 70% 55% at 50% 55%, var(--purple-glow) 0%, var(--purple-mid) 35%, var(--purple-dark) 70%, var(--purple-deep) 100%);
    font-family: "Questrial", "Century Gothic", sans-serif;
    overflow: hidden;
  }
  .damask-area {
    position: absolute; left: 100px; top: 230px; width: 400px; height: 360px;
    background: radial-gradient(ellipse at center, rgba(140, 70, 170, 0.22) 0%, rgba(140, 70, 170, 0) 70%);
  }
  .brand {
    position: absolute; left: 0; right: 0; top: 36px;
    text-align: center; color: var(--logo-tint);
    font-family: "Questrial", "Century Gothic", sans-serif;
  }
  .brand-dot {
    display: block; width: 44px; height: 44px; margin: 0 auto 22px;
    border-radius: 50%; background: var(--logo-tint);
  }
  .brand-name { font-size: 48px; line-height: 1; letter-spacing: 1px; }
  .brand-sub { font-size: 22px; margin-top: 8px; letter-spacing: 2px; }
  .contact {
    position: absolute; left: 213px; top: 326px;
    color: var(--contact-white); font-size: 14px; line-height: 19px;
  }
  .contact-name { font-size: 16px; padding-left: 16px; line-height: 21px; }
  .contact-line { display: flex; align-items: center; gap: 5px; }
  .contact-line svg { width: 11px; height: 11px; flex: none; }
  .social-square { width: 9px; height: 9px; margin: 0 2px 0 1px; background: var(--contact-white); flex: none; }
  .headline {
    position: absolute; left: 0; right: 0; top: 498px;
    text-align: center; color: var(--headline-tint);
    font-size: 19px; letter-spacing: 0.5px;
  }
  .feature-photo {
    position: absolute; left: 168px; top: 534px; width: 268px; height: 177px;
    background: linear-gradient(90deg, var(--photo-dark) 0%, #3a3a3a 35%, var(--photo-light) 65%, #2a2a2a 100%);
  }
  .right-page {
    position: relative; width: 60px; height: 741px;
    background: linear-gradient(180deg, var(--sky) 0%, #dfe5ea 38%, var(--foliage) 48%, #4f5a30 100%);
    overflow: hidden;
  }
  .caption {
    position: absolute; left: 6px; bottom: 10px;
    color: #ffffff; font-size: 11px; white-space: nowrap;
    font-family: "Questrial", "Century Gothic", sans-serif;
  }
</style>
</head>
<body>
  <main class="spread">
    <section class="left-page">
      <div class="damask-area" role="img" aria-label="Subtle damask pattern in lighter purple"></div>

      <header class="brand">
        <span class="brand-dot"></span>
        <div class="brand-name">Seabreeze</div>
        <div class="brand-sub">by Anton</div>
      </header>

      <address class="contact" style="font-style: normal;">
        <div class="contact-name">Anton</div>
        <div class="contact-line">
          <svg viewBox="0 0 12 12" aria-hidden="true"><path fill="currentColor" d="M1 4c0-2 2-3 5-3s5 1 5 3l-2 1-1-2H4L3 5 1 4zm2 2h6l1.5 4.5h-9L3 6zm3 1a1.4 1.4 0 1 0 0 2.8A1.4 1.4 0 0 0 6 7z"/></svg>
          <span>04 827 39 516</span>
        </div>
        <div class="contact-line">
          <svg viewBox="0 0 12 12" aria-hidden="true"><circle cx="6" cy="6" r="4.5" fill="none" stroke="currentColor" stroke-width="1.2"/><path d="M1.5 6h9M6 1.5c-2 2.5-2 6.5 0 9M6 1.5c2 2.5 2 6.5 0 9" fill="none" stroke="currentColor" stroke-width="0.9"/></svg>
          <span>www.amfoto.com.au</span>
        </div>
        <div class="contact-line">
          <span class="social-square"></span>
          <span>seabreezebyanton</span>
        </div>
      </address>

      <h2 class="headline" style="font-weight: normal;">Live, Dream, Love</h2>

      <div class="feature-photo" role="img" aria-label="Black and white photograph of a bride holding a bouquet beside a curtained window"></div>
    </section>

    <section class="right-page" role="img" aria-label="Full-page colour wedding photograph of a couple outdoors under a bright sky">
      <span class="caption">Seabreeze by Anton</span>
    </section>
  </main>
</body>
</html>
```